Harborline Network Solutions - IT Services Company/Managed Services/Consulting Card Design

Our company needs a business card design that will appeal to client companies with 50-1000 employees. We do IT services, administration, management, projects, budgeting and consulting (Like a small Quellbrook.com, Vantrelle.com or Drumvale.com). Mainly helping businesses use technology to be more competitive and efficient. We work with IT Infrastructure, switches, routers, firewalls and Cloud, Penwick/Tarvo servers, Kelpnode server virtualization, Datacenter environments, Email systems, Business Systems, Backup, Disaster Recovery, Data Security, ZPB, Workdesk 720 and Mistral.) Would like the final design to be professional but stand out to our prospective clients. Our current logo is attached. Color or design could be changed. Overall looking for a great finished product, original ideas are welcome and would pay more for the right one. If you think you have a better logo idea include a general idea if you can. Web design has not been done yet so that is a later possibility too.

Target Market(s)

1st - Mid-sized companies with 100-1000 employees with technology needs
2nd - Smaller companies with 20-99 employees with technology needs
- These companies can be in many different industries. Heathcare, legal, manufacturing, education, non-profit, services

Industry/Entity Type

Information Technology

Contact Information for Business Card

Should include the following info:

Logo or other logo with Company Name

Martin J. Calder

Principal

HarborlineNet.example

mcalder@HarborlineNet.example

(555) 7-HARBOR x 318

Font styles to use
Other font styles liked:
• designer can decide

Requirements
Must have
• Professional, appealing design, appeal to the target market
Nice to have
• Some sort of additional accent design that would stand out could be nice. I thought of adding a graphic in the top left corner that would look like the corner of the card was becoming more and more pixelated as it got near the corner, with some pixels missing.

```html
<!DOCTYPE html>
<html lang="en">
<head>
<meta charset="utf-8">
<title>Harborline Network Solutions – Business Card</title>
<link rel="stylesheet" href="https://fonts.googleapis.com/css2?family=EB+Garamond:wght@400;600&display=swap">
<style>
  :root {
    --backdrop: #1d1d1f;
    --card-white: #f7f7f8;
    --navy: #26287a;
    --navy-deep: #1b1c5e;
    --ink-blue: #3c4a7a;
    --slate: #5d6478;
    --silver: #e9ebf2;
    --rule: #b9bfd0;
  }
  * { box-sizing: border-box; margin: 0; padding: 0; }
  html, body { width: 1200px; height: 873px; overflow: hidden; }
  body {
    background: var(--backdrop);
    font-family: "EB Garamond", Georgia, serif;
    position: relative;
  }
  .card {
    position: absolute;
    width: 560px;
    height: 320px;
    border-radius: 16px;
    overflow: hidden;
    box-shadow: 0 18px 40px rgba(0,0,0,.55);
  }

  /* Company name: one colour, one weight, one plain square */
  .company {
    position: absolute;
    display: flex;
    align-items: center;
    font-weight: 600;
    line-height: 1.15;
  }
  .company__mark { flex: none; }

  /* Front */
  .card--front { left: 90px; top: 90px; background: var(--card-white); }
  .card--front .band {
    position: absolute; left: 0; right: 0; bottom: 0; height: 58px;
    background: var(--navy);
    border-top: 4px solid var(--navy-deep);
  }
  .card--front .company {
    left: 40px; top: 62px; width: 230px;
    gap: 12px; font-size: 21px; color: var(--ink-blue);
  }
  .card--front .company__mark { width: 14px; height: 14px; background: var(--ink-blue); }
  .divider {
    position: absolute; left: 290px; top: 50px; width: 1px; height: 150px;
    background: linear-gradient(var(--card-white), var(--rule), var(--card-white));
  }
  .contact { position: absolute; left: 316px; top: 64px; list-style: none; }
  .contact li {
    display: flex; align-items: center; gap: 10px;
    font-size: 14px; color: var(--slate); margin-bottom: 12px;
    white-space: nowrap;
  }
  .contact svg { width: 20px; height: 20px; flex: none; }
  .person { position: absolute; left: 40px; top: 182px; }
  .person .name { font-size: 22px; font-weight: 600; color: var(--ink-blue); }
  .person .role { font-size: 13px; color: var(--slate); text-align: right; }

  /* Back */
  .card--back {
    left: 550px; top: 460px;
    background: linear-gradient(135deg, var(--navy) 0%, var(--navy-deep) 100%);
    color: var(--silver);
  }
  .card--back .company {
    left: 46px; top: 58px; width: 470px;
    gap: 16px; font-size: 34px; color: var(--silver);
  }
  .card--back .company__mark { width: 22px; height: 22px; background: var(--silver); }
  .services { position: absolute; list-style: none; font-size: 17px; }
  .services--left { left: 90px; top: 196px; }
  .services--right { left: 330px; top: 196px; }
  .services li { display: flex; align-items: center; gap: 10px; margin-bottom: 8px; }
  .services svg { width: 18px; height: 18px; flex: none; }
</style>
</head>
<body>

<section class="card card--front" aria-label="Business card front">
  <p class="company"><span class="company__mark"></span>Harborline Network Solutions</p>
  <div class="divider"></div>
  <ul class="contact">
    <li>
      <svg viewBox="0 0 20 20"><circle cx="10" cy="10" r="10" fill="#3c4a7a"/><path d="M7 5.5l1.8 0 .7 2.3-1.1.8a6 6 0 0 0 3 3l.8-1.1 2.3.7v1.8c-4.5.4-8-3.1-7.5-7.5z" fill="#fff"/></svg>
      (555) 7-HARBOR x 318
    </li>
    <li>
      <svg viewBox="0 0 20 20"><circle cx="10" cy="10" r="10" fill="#3c4a7a"/><rect x="5" y="6.5" width="10" height="7" fill="none" stroke="#fff" stroke-width="1.2"/><path d="M5 6.5l5 4 5-4" fill="none" stroke="#fff" stroke-width="1.2"/></svg>
      mcalder@HarborlineNet.example
    </li>
    <li>
      <svg viewBox="0 0 20 20"><circle cx="10" cy="10" r="10" fill="#3c4a7a"/><path d="M8.5 11.5l3-3M9 7.5l1-1a2.2 2.2 0 0 1 3.2 3.2l-1 1M11 12.5l-1 1a2.2 2.2 0 0 1-3.2-3.2l1-1" fill="none" stroke="#fff" stroke-width="1.3" stroke-linecap="round"/></svg>
      www.HarborlineNet.example
    </li>
  </ul>
  <div class="person">
    <p class="name">Martin J. Calder</p>
    <p class="role">Principal</p>
  </div>
  <div class="band"></div>
</section>

<section class="card card--back" aria-label="Business card back">
  <p class="company"><span class="company__mark"></span>Harborline Network Solutions</p>
  <ul class="services services--left">
    <li><svg viewBox="0 0 18 18"><circle cx="9" cy="9" r="9" fill="#e9ebf2"/><path d="M5 9.3l2.7 2.6L13 6.4" fill="none" stroke="#26287a" stroke-width="2"/></svg>IT services</li>
    <li><svg viewBox="0 0 18 18"><circle cx="9" cy="9" r="9" fill="#e9ebf2"/><path d="M5 9.3l2.7 2.6L13 6.4" fill="none" stroke="#26287a" stroke-width="2"/></svg>Administration</li>
    <li><svg viewBox="0 0 18 18"><circle cx="9" cy="9" r="9" fill="#e9ebf2"/><path d="M5 9.3l2.7 2.6L13 6.4" fill="none" stroke="#26287a" stroke-width="2"/></svg>Management</li>
  </ul>
  <ul class="services services--right">
    <li><svg viewBox="0 0 18 18"><circle cx="9" cy="9" r="9" fill="#e9ebf2"/><path d="M5 9.3l2.7 2.6L13 6.4" fill="none" stroke="#26287a" stroke-width="2"/></svg>Projects</li>
    <li><svg viewBox="0 0 18 18"><circle cx="9" cy="9" r="9" fill="#e9ebf2"/><path d="M5 9.3l2.7 2.6L13 6.4" fill="none" stroke="#26287a" stroke-width="2"/></svg>Budgeting</li>
    <li><svg viewBox="0 0 18 18"><circle cx="9" cy="9" r="9" fill="#e9ebf2"/><path d="M5 9.3l2.7 2.6L13 6.4" fill="none" stroke="#26287a" stroke-width="2"/></svg>Consulting</li>
  </ul>
</section>

</body>
</html>
```